Dental Design, very professional and noticable

Tindale Ridge Dental Surgery is based in Pelican Waters. We are a fast growing dental surgery and are looking for some professional business cards to send to patients.
We would like to see a design that is Vertical and uses the colours Soft Blue, Silver, White and Black. Maybe a full blue side with moto and details on back? Any other ideas or colours that you may think will make the card look unique is fine.
We need all details on the card that are listed above

Target Market(s)

Families, Retired, Other Professionals and Businesses

Industry/Entity Type

Dental

Contact Information for Business Card

Tindale Ridge Dental Surgery
Family, Cosmetic, Preventative
Dr. Owen Castrey
Dental Surgeon
BDS (Adel) FAE FADI FICD FPFA
phone: (07)50001846
fax: (07)50002917
email: tindaleridgedental@quillpost.com
http://tindaleridgedental.com/

Logo Text

Logo styles of interest
Abstract Logo
Requirements
Must have
• Vertical, Vibrant but Professional, Rounded Edges, Logo on front and back of card (different colours on each side)
Nice to have
• One side completely blue (not sure what shade) with logo and moto on bottom
Other side white, with blue or different coloured logo with details in black and silver?
Logo should show half circle with 1 end as arrow symbolizing pelican waters canal also a magnifine glass also half circled with 1 end as arrow. Any other ideas are welcome.
Should not have
• A tooth. A smile. Toothbrush or Toothpaste. Cornered edges.

```html
<!DOCTYPE html>
<html lang="en">
<head>
<meta charset="utf-8">
<title>Tindale Ridge Dental Surgery – Business Cards</title>
<link href="https://fonts.googleapis.com/css2?family=Open+Sans:wght@400;600;700&display=swap" rel="stylesheet">
<style>
  :root {
    --blue-top: #2f8fe0;
    --blue-light: #6cc0f0;
    --blue-pale: #a9dcf8;
    --blue-deep: #1566b8;
    --navy: #1c2f7a;
    --indigo: #3a3aa6;
    --silver: #b8c2cc;
    --white: #ffffff;
    --ink: #111111;
    --edge: #9aa3ad;
  }
  * { box-sizing: border-box; margin: 0; padding: 0; }
  html, body { width: 701px; height: 1200px; overflow: hidden; background: var(--white); }
  body { position: relative; font-family: "Open Sans", Arial, sans-serif; }

  .card {
    position: absolute;
    width: 300px; height: 555px;
    border-radius: 22px;
    overflow: hidden;
    border: 1px solid var(--edge);
    background: var(--white);
  }
  .card--front-a { left: 11px; top: 4px; background: linear-gradient(180deg, var(--blue-top) 0%, #5bb5ee 45%, #1c72c6 100%); }
  .card--back-a  { left: 390px; top: 4px; }
  .card--front-b { left: 11px; top: 638px; }
  .card--back-b  { left: 390px; top: 638px; }

  .blue-field {
    position: absolute; left: 0; right: 0; bottom: 0;
    background: linear-gradient(180deg, var(--blue-light) 0%, var(--blue-deep) 100%);
  }
  .swoosh-band {
    position: absolute; left: 0; right: 0;
    background: linear-gradient(180deg, rgba(169,220,248,0.35) 0%, rgba(169,220,248,0.85) 50%, rgba(108,192,240,0.4) 100%);
  }

  .card__content { position: absolute; inset: 0; text-align: center; }
  .line { position: absolute; left: 0; right: 0; text-align: center; }

  .mark { position: absolute; left: 50%; transform: translateX(-50%); display: flex; flex-direction: column; align-items: center; gap: 6px; }
  .mark__dot { width: 58px; height: 58px; border-radius: 50%; }
  .mark__name { font-size: 11px; font-weight: 600; letter-spacing: 1px; text-transform: uppercase; white-space: nowrap; }

  .practice { text-transform: uppercase; line-height: 1.3; }
  .practice--white { color: var(--white); font-size: 17px; font-weight: 400; }
  .practice--indigo { color: var(--indigo); font-size: 18px; font-weight: 400; }
  .practice--navy { color: var(--navy); font-size: 18px; font-weight: 700; }

  .tagline { color: var(--white); font-size: 15px; }

  .doctor { color: var(--ink); font-size: 21px; }
  .role { color: var(--ink); font-size: 16px; }
  .quals { color: var(--ink); font-size: 12px; }
  .contact { color: var(--ink); font-size: 14px; line-height: 1.55; }

  .header-b { position: absolute; left: 18px; right: 12px; top: 40px; display: flex; align-items: center; gap: 12px; }
  .header-b .mark__dot { width: 44px; height: 44px; background: var(--indigo); flex: none; }
  .header-b .practice--indigo { font-size: 17px; text-align: center; flex: 1; }
  .doctor--bold { color: var(--navy); font-size: 22px; font-weight: 600; }
  .role--navy { color: var(--navy); font-size: 17px; }
  .quals--navy { color: var(--navy); font-size: 12px; font-weight: 700; }
  .contact--white { color: var(--white); font-size: 14px; font-weight: 700; line-height: 1.6; }
</style>
</head>
<body>

<!-- Front, all blue -->
<section class="card card--front-a">
  <div class="swoosh-band" style="top:225px;height:70px" role="img" aria-label="Flowing water swoosh decoration"></div>
  <div class="card__content">
    <div class="mark" style="top:58px">
      <div class="mark__dot" style="background:var(--silver)"></div>
      <div class="mark__name" style="color:var(--white)">Tindale Ridge</div>
    </div>
    <div class="line practice practice--white" style="top:318px">Tindale Ridge<br>Dental<br>Surgery</div>
    <div class="line tagline" style="top:492px">Family, Cosmetic, Preventative</div>
  </div>
</section>

<!-- Back, white -->
<section class="card card--back-a">
  <div class="card__content">
    <div class="mark" style="top:30px">
      <div class="mark__dot" style="background:var(--indigo)"></div>
      <div class="mark__name" style="color:var(--indigo)">Tindale Ridge</div>
    </div>
    <div class="line practice practice--indigo" style="top:148px">Tindale Ridge<br>Dental Surgery</div>
    <div class="line doctor" style="top:318px">Dr. Owen Castrey</div>
    <div class="line role" style="top:350px">Dental Surgeon</div>
    <div class="line quals" style="top:378px">BDS (Adel) FAE FADI FICD FPFA</div>
    <div class="line contact" style="top:422px">phone: (07)50001846<br>fax: (07)50002917</div>
    <div class="line contact" style="top:478px">tindaleridgedental@quillpost.com<br>tindaleridgedental.com</div>
  </div>
</section>

<!-- Front, white top / blue bottom -->
<section class="card card--front-b">
  <div class="blue-field" style="top:205px"></div>
  <div class="swoosh-band" style="top:205px;height:65px" role="img" aria-label="Flowing water swoosh decoration"></div>
  <div class="card__content">
    <div class="line practice practice--navy" style="top:68px">Tindale Ridge<br>Dental<br>Surgery</div>
    <div class="mark" style="top:315px">
      <div class="mark__dot" style="background:var(--silver)"></div>
      <div class="mark__name" style="color:var(--white)">Tindale Ridge</div>
    </div>
    <div class="line tagline" style="top:492px">Family, Cosmetic, Preventative</div>
  </div>
</section>

<!-- Back, white top / blue bottom -->
<section class="card card--back-b">
  <div class="blue-field" style="top:210px"></div>
  <div class="swoosh-band" style="top:210px;height:65px" role="img" aria-label="Flowing water swoosh decoration"></div>
  <div class="card__content">
    <div class="header-b">
      <div class="mark__dot"></div>
      <div class="practice practice--indigo">Tindale Ridge<br>Dental Surgery</div>
    </div>
    <div class="line doctor--bold" style="top:112px">Dr. Owen Castrey</div>
    <div class="line role--navy" style="top:144px">Dental Surgeon</div>
    <div class="line quals--navy" style="top:172px">BDS (Adel) FAE FADI FICD FPFA</div>
    <div class="line contact--white" style="top:318px">phone: (07)50001846<br>fax: (07)50002917</div>
    <div class="line contact--white" style="top:405px">tindaleridgedental@quillpost.com<br>tindaleridgedental.com</div>
  </div>
</section>

</body>
</html>
```